依頼詳細
①一般的な広告デザインは避けたい
②文字や写真ではなく、全体のデザインで目を引くものを希望。
記載項目の文字もデザイナーのデザイン重視でフォント・サイズ変更ください
③斬新でシンプルなデザインを提案ください
④受講対象は退職前後の一部上場企業勤務のご夫婦、公務員、教員、企業役員や経営者、その妻など、アッパー層を対象としています。
それなりに老後資金はあるが、それをどのように計画的に使っていったり、また子供や孫の世代へ継承していけば良いかを考えている方たちが目を引くデザイン希望
⑤HPを記載しておきます。参考にしてください。
https://soyokaze-example.or.jp/

記載項目
(詳細は添付データに記載)
◼️キャッチフレーズ「定年後8割が悩む 老後資金の活かし方」
サブキャッチ「楽しく使い賢くツナグ~子や孫へ~」
◼️講座名 「老後資金の計算法&活用法」
◼️カリキュラム 添付データに記載
◼️リード文 添付データに記載
◼️ロゴ データ添付
◼️8/2 10:00~11:30(受付開始 9:30)
◼️定員 10組 受講料無料
◼️講師 相続診断認定講師
◼️申込締切 7/29(水)
◼️申込み お問合わせ①QRデータ添付(まだ作成出来ないため、後日送ります)②フリーダイヤル0120-555-193
③FAXでのお申込み欄を設ける。→06-6000-4417までFAX下さい
◼️団体案内(目立たせる必要はなく、記載があればOK。デザイナーの皆さんのデザイン優先してください。)
【主催】そよかぜ 一般社団法人みのり家計相談協議会
事務局:大阪市此花区緑丘5-2-6-312
TEL/06-6000-4416 FAX/06-6000-4417
サイズ
A4
ページ数
片面
希望イメージ
シンプル 複雑
単色 カラフル
暗い 明るい
日常 高級
遊び心 厳粛
未来的 伝統的
女性的 男性的
希望する色
緑系、茶系
納品ファイル
• イラストレーター形式 (.ai)
• PNG形式 (.png)
補足説明
.aiは、アウトライン化したものもデータを下さい。

過去の実績や、作品を確認させていただいたときに、とてもデザインの幅も広く、依頼者の要望に合わせてデザインをしていただけると感じました。
また、クラフタスの中での実績もかなりあり、とっても信頼できるデザイナーさんだと感じましたので、是非お願いしたいと思いました。

ご提案いただいたみなさま、本当に様々なご提案ありがとうございました。
とても色んなデザインを拝見でき、今後の参考にもなりました!
また、機会があればよろしくお願いいたします。

```html
<!DOCTYPE html>
<html lang="ja">
<head>
<meta charset="utf-8">
<title>老後資金の活かし方 セミナー</title>
<link rel="stylesheet" href="https://fonts.googleapis.com/css2?family=Noto+Sans+JP:wght@400;500;700;900&family=Noto+Serif+JP:wght@500;700;900&family=Oswald:wght@500;700&display=swap">
<style>
:root{
  --ink:#1d2419;
  --orange:#ef8d1f;
  --green:#5b8a33;
  --leaf:#b7cf3a;
  --circle:#1b1b1b;
  --photo-a:#8f8c86;
  --photo-b:#cfccc4;
  --rule:#6f8f4a;
  --paper:#ffffff;
}
*{margin:0;padding:0;box-sizing:border-box}
html,body{width:878px;height:1200px;overflow:hidden;background:var(--paper)}
.flyer{position:relative;width:878px;height:1200px;overflow:hidden;font-family:"Noto Sans JP",sans-serif;color:var(--ink)}
.tagline{position:absolute;left:30px;top:30px;font-size:14px;letter-spacing:1px}
.org-mark{position:absolute;right:30px;top:24px;display:flex;align-items:center;gap:8px;font-size:15px;font-weight:700;color:var(--green)}
.org-mark .dot{width:34px;height:34px;border-radius:50%;background:var(--orange)}
.lead{position:absolute;left:40px;top:80px;height:360px;writing-mode:vertical-rl;font-size:14px;line-height:1.9;letter-spacing:1px;color:#333}
.catch-circle{position:absolute;left:560px;top:120px;width:320px;height:320px;border-radius:50%;background:var(--circle)}
.catch-pre{position:absolute;left:318px;top:140px;writing-mode:vertical-rl;font-family:"Noto Serif JP",serif;font-weight:700;font-size:34px;color:var(--orange);letter-spacing:4px}
.catch-eight{position:absolute;left:365px;top:-10px;font-family:"Oswald",sans-serif;font-weight:700;font-size:270px;line-height:1;color:var(--orange)}
.catch-wari{position:absolute;left:500px;top:95px;font-family:"Noto Serif JP",serif;font-weight:900;font-size:130px;line-height:1;color:var(--ink)}
.catch-ga{position:absolute;left:640px;top:150px;font-family:"Noto Serif JP",serif;font-weight:900;font-size:60px;color:#fff}
.catch-mu{position:absolute;left:770px;top:225px;font-family:"Noto Serif JP",serif;font-weight:900;font-size:50px;color:#fff}
.catch-nayamu{position:absolute;left:640px;top:225px;font-family:"Noto Serif JP",serif;font-weight:900;font-size:140px;line-height:1;color:#fff}
.subcatch{position:absolute;left:340px;top:290px;transform:rotate(-14deg);transform-origin:left top;font-family:"Noto Serif JP",serif;font-weight:700;text-align:center}
.subcatch .l1{font-size:26px;color:var(--green)}
.subcatch .l2{font-size:30px;color:var(--orange)}
.title{position:absolute;right:30px;top:395px;text-align:right;font-family:"Noto Serif JP",serif;font-weight:900;font-size:82px;line-height:1.05;color:var(--ink)}
.title .accent{color:var(--orange)}
.course{position:absolute;right:30px;top:570px;font-family:"Noto Serif JP",serif;font-weight:700;font-size:34px;color:var(--green)}
.curriculum{position:absolute;left:50px;top:600px}
.curriculum h2{font-family:"Noto Serif JP",serif;font-size:38px;color:var(--green);font-weight:700;margin-bottom:14px;border-bottom:2px solid var(--rule);display:inline-block;padding-bottom:2px}
.curriculum ol{list-style:none}
.curriculum li{display:flex;align-items:center;gap:12px;font-size:22px;font-weight:500;height:38px}
.curriculum .num{width:28px;height:28px;background:var(--leaf);color:#fff;font-weight:700;font-size:18px;display:flex;align-items:center;justify-content:center}
.lecturer-photo{position:absolute;right:0;top:745px;width:322px;height:330px;background:linear-gradient(160deg,var(--photo-b),var(--photo-a))}
.date{position:absolute;left:40px;top:905px;font-family:"Oswald",sans-serif;font-weight:700;font-size:150px;line-height:1;color:var(--orange)}
.time{position:absolute;left:292px;top:935px;color:var(--green);font-weight:700}
.time .hours{font-family:"Oswald",sans-serif;font-size:46px;line-height:1}
.time .open{font-size:18px;display:block;margin-top:2px}
.details{position:absolute;left:292px;top:1010px;font-size:16px;line-height:1.55}
.apply{position:absolute;left:30px;top:1082px;width:818px;font-size:17px;font-weight:700;color:var(--green);display:flex;align-items:baseline;gap:10px;border-top:2px solid var(--rule);padding-top:4px}
.apply .big{font-family:"Oswald",sans-serif;font-size:26px;color:var(--ink)}
.form{position:absolute;left:30px;top:1118px;width:818px;border-collapse:collapse;font-size:13px}
.form td{border:1px solid var(--rule);height:24px;padding:0 6px}
.form .label{width:80px;background:#eef3e4;color:var(--green);font-weight:700}
.form .label.r{width:90px}
.footer{position:absolute;left:30px;top:1174px;width:818px;font-size:11px;color:#444;line-height:1.4}
</style>
</head>
<body>
<div class="flyer">
  <p class="tagline">人生を楽しむ大人の「学び場」</p>
  <div class="org-mark"><span class="dot"></span>そよかぜ</div>

  <p class="lead">老後資金は十分にあるはずなのに、<br>どう使えばよいか迷っていませんか。<br>ご夫婦の豊かな暮らしと、<br>子や孫へ賢くつなぐための<br>計算と活用の考え方を、<br>わかりやすくお伝えします。</p>

  <div class="catch-circle"></div>
  <div class="catch-pre">定年後</div>
  <div class="catch-eight">8</div>
  <div class="catch-wari">割</div>
  <div class="catch-ga">が</div>
  <div class="catch-nayamu">悩</div>
  <div class="catch-mu">む</div>

  <div class="subcatch">
    <div class="l1">楽しく使い賢くツナグ</div>
    <div class="l2">〜子や孫へ〜</div>
  </div>

  <h1 class="title">老後資金<span class="accent">の</span><br>活かし方</h1>
  <p class="course">老後資金の計算法&amp;活用法</p>

  <section class="curriculum">
    <h2>カリキュラム</h2>
    <ol>
      <li><span class="num">1</span>意外と知らない老後資金計画</li>
      <li><span class="num">2</span>気になる隣の家の老後資金</li>
      <li><span class="num">3</span>相続セミナーが流行る理由</li>
      <li><span class="num">4</span>相続・終活など必要？</li>
      <li><span class="num">5</span>10年あればお金は育つ</li>
      <li><span class="num">6</span>老後資金計画で人生が楽しくなる</li>
    </ol>
  </section>

  <div class="lecturer-photo" role="img" aria-label="講師の写真"></div>

  <div class="date">8/2</div>
  <div class="time"><span class="hours">10:00〜11:30</span><span class="open">(受付開始 9:30)</span></div>
  <div class="details">定員：10組 受講料無料<br>講師：相続診断認定講師<br>申込締切 7/29(水)</div>

  <div class="apply">お申込みは <span class="big">0120-555-193</span> または <span class="big">FAX 06-6000-4417</span> または QRコードから</div>

  <table class="form">
    <tr><td class="label">お名前</td><td></td><td class="label r">電話番号</td><td></td></tr>
    <tr><td class="label">住所</td><td></td><td class="label r">FAX番号</td><td></td></tr>
  </table>

  <p class="footer">【主催】そよかぜ 一般社団法人みのり家計相談協議会　事務局：大阪市此花区緑丘5-2-6-312　TEL/06-6000-4416　FAX/06-6000-4417</p>
</div>
</body>
</html>
```